Web Design for photo printing service

Hi
I am looking for a new web design theme for our almost ready website http://fotoblik.zrmq.net, it will soon be launched under the name: www.zuna.is. (ZUNA means: You Only Live Once)

This is a website focused on printing photo products like: photo books, Greeting cards, posters, etc.

The whole theme should be playful, fun, creative. The marketing will be is that Life is fun, keep your memories. remember the good time etc.

So what I am looking for is a simple, yet colorful theme, easy to use.

We will be running max 4- 6 product groups, all extra info should be on the button,
expect shopping chart and sign in should be on top.

Extra feature:
Once a year during christmas, the web will turn on christmas outfit, it transforms
to Christmas looking Web. So a X-mas version would be fun to see !

Target Market(s)

Young people 20-35, young families.

Industry/Entity Type

Printing

Requirements
Must have
• Fun looking colorful design, simple to use.
Should not have
• Dark heavy look

```html
<!DOCTYPE html>
<html lang="en">
<head>
<meta charset="utf-8">
<title>Zuna – Printing Photo Products</title>
<link rel="stylesheet" href="https://fonts.googleapis.com/css2?family=Roboto:wght@400;500&family=PT+Sans:wght@400&display=swap">
<style>
  :root {
    --orange: #f39a2e;
    --orange-light: #f8b458;
    --orange-dark: #e6831a;
    --peach: #f6c79c;
    --peach-light: #fbe1c8;
    --purple: #a0137f;
    --purple-dark: #7e0c63;
    --text-grey: #6f6f6f;
    --border-grey: #d9d9d9;
    --footer-bg: #ececec;
    --white: #ffffff;
    --brand-teal: #29a3c9;
  }
  * { box-sizing: border-box; margin: 0; padding: 0; }
  html, body { width: 1200px; height: 1050px; overflow: hidden; background: var(--white); }
  body { position: relative; font-family: "PT Sans", sans-serif; color: var(--text-grey); }

  .site-header { position: absolute; left: 0; top: 0; width: 1200px; height: 106px; }
  .brand { position: absolute; left: 122px; top: 22px; display: flex; align-items: center; gap: 12px; }
  .brand-dot { width: 22px; height: 22px; border-radius: 50%; background: var(--purple); }
  .brand-name { font-family: "Roboto", sans-serif; font-weight: 500; font-size: 56px; line-height: 1; color: var(--brand-teal); letter-spacing: 2px; }

  .social { position: absolute; left: 983px; top: 8px; display: flex; gap: 5px; }
  .social span { width: 20px; height: 20px; display: block; }
  .social .s1 { background: #3b5998; }
  .social .s2 { background: #1da1f2; }
  .social .s3 { background: #d62b24; }
  .social .s4 { background: #333; }

  .cart { position: absolute; left: 910px; top: 43px; width: 172px; height: 47px; border: 1px solid #e3e3e3; display: flex; align-items: center; padding-left: 7px; }
  .cart svg { margin-right: 12px; }
  .cart-label { font-size: 13px; line-height: 17px; color: #999; }
  .cart-label strong { font-weight: 400; display: block; }

  .main-nav { position: absolute; left: 0; top: 106px; width: 1200px; height: 42px; background: linear-gradient(var(--orange-light), var(--orange)); border-bottom: 1px solid var(--orange-dark); }
  .main-nav ul { list-style: none; }
  .main-nav li { position: absolute; top: 12px; font-family: "Roboto", sans-serif; font-weight: 500; font-size: 14px; line-height: 18px; color: var(--white); white-space: nowrap; }
  .nav-books { left: 140px; }
  .nav-calendars { left: 278px; }
  .nav-posters { left: 399px; }
  .nav-map { left: 501px; }
  .nav-prints { left: 570px; }
  .nav-price { left: 777px; }
  .btn-register, .btn-signin { position: absolute; top: 7px; height: 28px; font-family: "Roboto", sans-serif; font-weight: 500; font-size: 14px; color: var(--white); display: flex; align-items: center; justify-content: center; }
  .btn-register { left: 900px; width: 90px; background: var(--purple); border: 1px solid var(--purple-dark); }
  .btn-signin { left: 999px; width: 80px; background: var(--orange); border: 1px solid #fbd29d; }

  .hero { position: absolute; left: 0; top: 148px; width: 1200px; height: 450px; background: linear-gradient(180deg, var(--peach-light), var(--peach) 60%, #f3b886); }
  .hero-slide { position: absolute; left: 120px; top: 20px; width: 960px; height: 380px; background: linear-gradient(90deg, #e9e2e2 0%, #8a8a8a 40%, #2c2c2c 70%, #6a6a6a 100%); box-shadow: 0 12px 14px -8px rgba(0,0,0,.35); }
  .slide-dots { position: absolute; left: 440px; top: 347px; width: 87px; height: 22px; border-radius: 11px; background: rgba(120,120,120,.7); display: flex; align-items: center; justify-content: center; gap: 5px; }
  .slide-dots span { width: 10px; height: 10px; border-radius: 50%; background: #d8d8d8; }

  .products-title { position: absolute; left: 118px; top: 624px; font-family: "Roboto", sans-serif; font-weight: 400; font-size: 14px; line-height: 16px; color: var(--orange); }
  .pager { position: absolute; left: 1037px; top: 631px; display: flex; gap: 5px; }
  .pager span { width: 10px; height: 10px; border-radius: 50%; background: #999; border: 1px solid #666; }
  .pager span.active { background: #444; }

  .product-card { position: absolute; top: 665px; width: 300px; height: 302px; border: 1px solid var(--border-grey); text-align: center; }
  .product-card:nth-of-type(1) { left: 119px; }
  .product-card:nth-of-type(2) { left: 449px; }
  .product-card:nth-of-type(3) { left: 779px; }
  .product-image { width: 130px; height: 110px; margin: 22px auto 0; border-radius: 3px; }
  .img-books { background: linear-gradient(135deg, #d8d8d8, #9a8560 60%, #eaeaea); }
  .img-calendar { width: 64px; background: linear-gradient(180deg, #5c3a20 0%, #a4642c 45%, #e6ef9a 55%, #c9e06c 100%); }
  .img-posters { width: 90px; background: linear-gradient(160deg, #8fcbe0 0%, #c46a3a 55%, #2e241d 100%); }
  .product-name { margin-top: 19px; font-family: "Roboto", sans-serif; font-weight: 400; font-size: 14px; line-height: 16px; color: var(--orange); }
  .product-text { margin-top: 9px; font-size: 11.5px; line-height: 14.5px; color: var(--text-grey); white-space: nowrap; }
  .product-price { margin-top: 8px; font-family: "Roboto", sans-serif; font-weight: 500; font-size: 13px; line-height: 16px; color: var(--orange); }
  .btn-more { display: inline-flex; align-items: center; justify-content: center; margin-top: 12px; width: 90px; height: 27px; background: var(--purple); border: 1px solid var(--purple-dark); font-family: "Roboto", sans-serif; font-weight: 500; font-size: 12.5px; color: var(--white); }

  .site-footer { position: absolute; left: 0; top: 1001px; width: 1200px; height: 49px; background: var(--footer-bg); font-size: 11.5px; color: #666; }
  .footer-links { position: absolute; left: 121px; top: 18px; }
  .copyright { position: absolute; right: 124px; top: 18px; }
</style>
</head>
<body>
  <header class="site-header">
    <div class="brand"><span class="brand-name">ZUNA</span><span class="brand-dot"></span></div>
    <div class="social"><span class="s1"></span><span class="s2"></span><span class="s3"></span><span class="s4"></span></div>
    <div class="cart">
      <svg width="30" height="26" viewBox="0 0 30 26" aria-hidden="true">
        <path d="M2 8h26l-4 14H6z" fill="#2fb34a"/>
        <path d="M9 8l5-6M21 8l-5-6" stroke="#2fb34a" stroke-width="2" fill="none"/>
        <path d="M5 13h20M6 17h18" stroke="#fff" stroke-width="1.5"/>
      </svg>
      <div class="cart-label"><strong>MY CART</strong>0 Articles • kr 0.00</div>
    </div>
  </header>

  <nav class="main-nav">
    <ul>
      <li class="nav-books">PHOTO BOOKS</li>
      <li class="nav-calendars">CALENDARS</li>
      <li class="nav-posters">POSTERS</li>
      <li class="nav-map">MAP</li>
      <li class="nav-prints">PRINTED PHOTOGRAPHS</li>
      <li class="nav-price">OUR PRICE</li>
    </ul>
    <span class="btn-register">REGISTER</span>
    <span class="btn-signin">SIGN IN</span>
  </nav>

  <section class="hero" role="img" aria-label="Peach background with light plant silhouettes">
    <div class="hero-slide" role="img" aria-label="Open wedding photo book beside a rose-decorated wedding cake">
      <div class="slide-dots"><span></span><span></span><span></span><span></span><span></span></div>
    </div>
  </section>

  <h2 class="products-title">PRINTING PHOTO PRODUCTS</h2>
  <div class="pager"><span></span><span class="active"></span><span></span></div>

  <article class="product-card">
    <div class="product-image img-books" role="img" aria-label="Open photo book"></div>
    <h3 class="product-name">PHOTO BOOKS</h3>
    <p class="product-text">Your own photographs? Why? We know that your<br>images deserve to be preserved. Even probably the best<br>pictures in the world - so practically....</p>
    <p class="product-price">FROM KR 2000,00</p>
    <span class="btn-more">MORE INFO</span>
  </article>
  <article class="product-card">
    <div class="product-image img-calendar" role="img" aria-label="Wall calendar with autumn photo"></div>
    <h3 class="product-name">CALENDARS</h3>
    <p class="product-text">Your own photographs? Why? We know that your<br>images deserve to be preserved. Even probably the best<br>pictures in the world - so practically....</p>
    <p class="product-price">FROM KR 2000,00</p>
    <span class="btn-more">MORE INFO</span>
  </article>
  <article class="product-card">
    <div class="product-image img-posters" role="img" aria-label="Stack of printed poster photos"></div>
    <h3 class="product-name">POSTERS</h3>
    <p class="product-text">Your own photographs? Why? We know that your<br>images deserve to be preserved. Even probably the best<br>pictures in the world - so practically....</p>
    <p class="product-price">FROM KR 2000,00</p>
    <span class="btn-more">MORE INFO</span>
  </article>

  <footer class="site-footer">
    <div class="footer-links">Home | The small print | What do you want to know | Rates | About Us | Contact</div>
    <div class="copyright">©2013 Zuna | All Rights Reserved.</div>
  </footer>
</body>
</html>
```